Locksmiths Business Card Designs needed!!

I need a business card design for my new small locksmith business.
I would love my business card to be simple, (not too many photos of locks or keys) but strong images so that everyone can recognise it is locksmithing business without reading the words.

I want all information i put in upper article to appear on front side in anyway depending on your design of suggestions and on the back side I would love to mention theses;
-24 /7 mobile services (including weekends & public holidays)
-Residential / Commercial/ Automotive
-Opening / Repair / Installation
-Cut keys

Im not a native english speaker so you can fix the words or expressions as you think it is right and natural.

I realised that in the business names, there is too many "locks" and "s" so I would love to seperate the words somehow so that it is more natural when someone read the business name on the card. for example,put the part of "Bright Harbour Trade Services" first line and the part of "Locksmiths" on the other line....I am just suggesting..doesn't need to be like that..but it should say "Locksmiths" as it is locksmiths business. :)

Target Market(s)

all generations

Industry/Entity Type

Locksmith

Contact Information for Business Card

business name : Bright Harbour Trade Services Locksmiths
ABN 46281903754
Name : Tom Reyes (바다 문)
phone : 0468 219 357
email : brightharbourtrade@mailvero.net

Requirements
Must have
• A symbol of either a key or a lock
Nice to have
• I like the symbol of a key in the photo I have attached here. So maybe, if you couldn't find any other good symbols I am happy to have the symbol on the business somehow.
Should not have
• Too many keys or locks

```html
<!DOCTYPE html>
<html lang="en">
<head>
<meta charset="utf-8">
<title>Bright Harbour Trade Services Locksmiths – Business Card</title>
<link rel="stylesheet" href="https://fonts.googleapis.com/css2?family=Arimo:wght@400;700&family=Noto+Sans+KR:wght@400;700&display=swap">
<style>
  :root {
    --page: #ffffff;
    --leather-light: #a5452a;
    --leather-mid: #8f3a22;
    --leather-dark: #6e2a18;
    --gold: #d6b52a;
    --gold-soft: #e6cf6a;
    --gold-line: #c9a43a;
    --maroon: #5a0e0e;
    --band-top: #a84a08;
    --band-mid: #e07d10;
    --band-bottom: #b85a06;
    --band-text: #f6e08a;
    --ink: #111111;
    --key-light: #f4dc7a;
    --key-dark: #c79a24;
  }
  * { box-sizing: border-box; margin: 0; padding: 0; }
  html, body {
    width: 1200px;
    height: 367px;
    overflow: hidden;
    background: var(--page);
  }
  body {
    position: relative;
    font-family: "Arimo", Arial, sans-serif;
  }
  .card {
    position: absolute;
    top: 12px;
    width: 577px;
    height: 327px;
    background: radial-gradient(ellipse at 40% 35%, var(--leather-light) 0%, var(--leather-mid) 55%, var(--leather-dark) 100%);
    box-shadow: 0 1px 4px rgba(0,0,0,0.35);
    overflow: hidden;
  }
  .card--front { left: 12px; }
  .card--back { left: 611px; }

  .contact-band {
    position: absolute;
    left: 0;
    right: 0;
    top: 211px;
    height: 37px;
    background: linear-gradient(to bottom, var(--band-top) 0%, var(--band-mid) 45%, var(--band-bottom) 100%);
  }
  .key-symbol {
    position: absolute;
    left: 44px;
    top: 18px;
    width: 92px;
    height: 282px;
    border-radius: 40px 40px 10px 10px;
    background: linear-gradient(to right, var(--key-light), var(--key-dark));
  }
  .business-name {
    position: absolute;
    left: 154px;
    top: 30px;
    font-size: 18px;
    letter-spacing: 1.5px;
    color: var(--gold);
    text-transform: uppercase;
    white-space: nowrap;
  }
  .business-type {
    position: absolute;
    left: 229px;
    top: 64px;
    font-size: 24px;
    font-weight: 700;
    letter-spacing: 8px;
    color: var(--maroon);
    text-transform: uppercase;
  }
  .owner-name {
    position: absolute;
    right: 12px;
    top: 131px;
    font-size: 21px;
    font-weight: 700;
    color: var(--gold-soft);
    white-space: nowrap;
  }
  .owner-name .korean {
    font-family: "Noto Sans KR", sans-serif;
    font-weight: 700;
  }
  .abn {
    position: absolute;
    right: 30px;
    top: 168px;
    font-size: 19px;
    color: var(--gold-soft);
  }
  .contact-line {
    position: absolute;
    left: 148px;
    top: 220px;
    font-size: 16px;
    color: var(--band-text);
    white-space: nowrap;
  }
  .contact-line .divider {
    display: inline-block;
    width: 2px;
    height: 21px;
    background: var(--band-text);
    margin: 0 7px;
    vertical-align: -4px;
  }

  .service-frame {
    position: absolute;
    left: 19px;
    top: 18px;
    right: 19px;
    bottom: 18px;
    border: 1px solid var(--gold-line);
  }
  .service-list {
    position: absolute;
    left: 79px;
    top: 80px;
    list-style: none;
    font-size: 19px;
    color: var(--ink);
    line-height: 36px;
  }
  .service-list li {
    position: relative;
    padding-left: 41px;
  }
  .service-list li.has-bullet::before {
    content: "";
    position: absolute;
    left: 0;
    top: 15px;
    width: 6px;
    height: 6px;
    background: var(--ink);
  }
</style>
</head>
<body>
  <section class="card card--front">
    <div class="contact-band"></div>
    <div class="key-symbol" role="img" aria-label="Illustration of a golden key standing upright"></div>
    <h1 class="business-name">Bright Harbour Trade Services</h1>
    <p class="business-type">Locksmiths</p>
    <p class="owner-name">Tom Reyes (<span class="korean">바다 문</span>)</p>
    <p class="abn">ABN 46281903754</p>
    <p class="contact-line">Ph: 0468 219 357<span class="divider"></span>brightharbourtrade@mailvero.net</p>
  </section>

  <section class="card card--back">
    <div class="service-frame"></div>
    <ul class="service-list">
      <li class="has-bullet">24 /7 mobile services</li>
      <li>(Including weekends &amp; public holidays)</li>
      <li class="has-bullet">Residential / Commercial/ Automotive</li>
      <li class="has-bullet">Opening / Repair / Installation</li>
      <li class="has-bullet">Cut keys</li>
    </ul>
  </section>
</body>
</html>
```